Brightwire Hollow Business cards

one side I would like my logo (uploaded) and the other side I want my details. I'm an electrician in sydney. The logo side I'm happy with just a white background and our logo in the middle.

Details for other side
24/7 Sydney Electrician
Marcus Pell
0431 587 219
marcus@brightwirehollow.com.au
brightwirehollow.com.au
icons for facebook, instagram, linked in

Industry/Entity Type

electrician

Contact Information for Business Card

company info

```html
<!DOCTYPE html>
<html lang="en">
<head>
<meta charset="utf-8">
<title>Brightwire Hollow – Business Cards</title>
<link href="https://fonts.googleapis.com/css2?family=Montserrat:wght@400;500;800&display=swap" rel="stylesheet">
<style>
  :root {
    --stage: #2a2a2a;
    --card: #0e0e0e;
    --red: #ee3524;
    --white: #ffffff;
    --muted: #d9d9d9;
  }
  html, body {
    margin: 0;
    width: 1200px;
    height: 875px;
    overflow: hidden;
    background: var(--stage);
    font-family: "Montserrat", sans-serif;
  }
  .canvas {
    position: relative;
    width: 1200px;
    height: 875px;
  }
  .card {
    position: absolute;
    width: 520px;
    height: 297px;
    background: var(--card);
    border-radius: 18px;
    overflow: hidden;
    box-shadow: 0 18px 40px rgba(0,0,0,.45);
  }
  .card-front { left: 70px; top: 140px; }
  .card-back  { left: 610px; top: 438px; }

  .wordmark {
    font-weight: 800;
    color: var(--red);
    letter-spacing: 1px;
    text-transform: uppercase;
    margin: 0;
    line-height: 1.05;
  }
  .card-front .wordmark {
    position: absolute;
    inset: 0;
    display: flex;
    align-items: center;
    justify-content: center;
    text-align: center;
    font-size: 46px;
  }

  .badge {
    position: absolute;
    left: -70px;
    top: 38px;
    width: 230px;
    height: 230px;
    border-radius: 50%;
    background: var(--red);
  }

  .details {
    position: absolute;
    left: 196px;
    top: 28px;
    right: 24px;
    bottom: 20px;
    color: var(--white);
  }
  .details .wordmark { font-size: 24px; margin-bottom: 14px; }
  .rule { height: 2px; background: var(--red); margin: 8px 0; }
  .person { margin: 6px 0; }
  .person-name {
    color: var(--red);
    font-weight: 800;
    font-size: 17px;
    margin: 0;
  }
  .line {
    display: flex;
    align-items: center;
    gap: 8px;
    font-size: 12px;
    font-weight: 500;
    color: var(--muted);
    margin: 3px 0;
  }
  .line svg { width: 12px; height: 12px; flex: none; fill: var(--red); }
  .tagline {
    font-size: 12px;
    font-weight: 500;
    text-transform: uppercase;
    color: var(--muted);
    margin: 6px 0 0 20px;
  }
  .social {
    position: absolute;
    right: 0;
    bottom: 0;
    display: flex;
    gap: 8px;
  }
  .social span {
    width: 16px;
    height: 16px;
    border-radius: 4px;
    background: var(--red);
  }
</style>
</head>
<body>
<main class="canvas">

  <section class="card card-front" aria-label="Business card front">
    <h1 class="wordmark">Brightwire<br>Hollow</h1>
  </section>

  <section class="card card-back" aria-label="Business card back">
    <div class="badge" aria-hidden="true"></div>
    <div class="details">
      <h2 class="wordmark">Brightwire Hollow</h2>
      <div class="rule"></div>
      <div class="person">
        <p class="person-name">Marcus Pell</p>
        <p class="line"><svg viewBox="0 0 24 24"><path d="M6.6 10.8a15 15 0 0 0 6.6 6.6l2.2-2.2c.3-.3.7-.4 1-.2 1.1.4 2.3.6 3.6.6.6 0 1 .4 1 1V20c0 .6-.4 1-1 1A17 17 0 0 1 3 4c0-.6.4-1 1-1h3.5c.6 0 1 .4 1 1 0 1.3.2 2.5.6 3.6.1.3 0 .7-.2 1z"/></svg>0431 587 219</p>
      </div>
      <div class="rule"></div>
      <div class="person">
        <p class="person-name">Lena Voss</p>
        <p class="line"><svg viewBox="0 0 24 24"><path d="M6.6 10.8a15 15 0 0 0 6.6 6.6l2.2-2.2c.3-.3.7-.4 1-.2 1.1.4 2.3.6 3.6.6.6 0 1 .4 1 1V20c0 .6-.4 1-1 1A17 17 0 0 1 3 4c0-.6.4-1 1-1h3.5c.6 0 1 .4 1 1 0 1.3.2 2.5.6 3.6.1.3 0 .7-.2 1z"/></svg>0452 316 884</p>
      </div>
      <div class="rule"></div>
      <p class="line"><svg viewBox="0 0 24 24"><path d="M2 5h20v14H2z M2 5l10 8 10-8" /></svg>service@brightwirehollow.com.au</p>
      <p class="line"><svg viewBox="0 0 24 24"><circle cx="12" cy="12" r="10"/></svg>www.brightwirehollow.com.au</p>
      <p class="tagline">24/7 Sydney Electricians</p>
      <div class="social" aria-label="Social links"><span></span><span></span></div>
    </div>
  </section>

</main>
</body>
</html>
```